Business Card & Logo Design - Hedge Fund

We need a business card and logo design for a hedge fund. The hedge fund is named Morvane Equity LLC. Morvane Equity was created by finance professors and the strategy is based academic research that looks for patterns in stock prices. The design should look conservative, solid, strong. We favor a classic style - nothing flashy. The logo can relate to the name Morvane Equity, or it could involve a symbol design that connotes "science" . We are open to ideas. We do not want alot of colors - but if any, color - blue is preferred. The font that seems to look best for the name (Morvane Equity) is arial black. We are open to ideas. Most important - we want to see a mock up of an actual business card with the logo concept embedded. The business card should include space for : company name, individual name, position title, cell phone, address. We hope to have this work done by Sept. 8.

Target Market(s)

We will be meeting with and giving the business card to institutions and high net worth individuals.

Industry/Entity Type

Investment Advisory

Contact Information for Business Card

Company name - Morvane Equity LLC
Individual name - Peter Dalby
Title - Portfolio Manager
Cell - (412) 555-0187
Address - 2650 Birchmont Lane, Suite 300, Atlanta GA 30327

Font styles to use
Other font styles liked:
• Arial

Colors
3277b5
0255a3
85acd3
cedeed
fdf9cf
d9d9d9
e6e6e6
f04a50
6b449b

Requirements
Must have
• Must have card details that are sited above.
• We would like a logo related to the name (Morvane Equity) or concept of the fund.
Nice to have
• We want conservative / understated / clean crisp look.
• If any colors - we prefer conservative appearance - blue / gray.
• I have enclosed an example of a card style that looks attractive - please do not exactly copy this card. This is not our company or logo. I feel the layout is attractive - just as an example
Should not have
• Avoid too much color.
• I have selected some preferred colors. Please do not use all of the colors - I have selected a few that might work - but I am not sure. We are open to your ideas so please do not feel the need to use all or any of these.

```html
<!DOCTYPE html>
<html lang="en">
<head>
<meta charset="utf-8">
<title>Morvane Equity LLC – Business Card</title>
<link rel="stylesheet" href="https://fonts.googleapis.com/css2?family=Arimo:wght@400;700&display=swap">
<style>
  :root {
    --navy: #0b3668;
    --ink: #0d3a6b;
    --steel: #4f7aa6;
    --rule: #85acd3;
    --brand-blue: #0255a3;
    --paper: #ffffff;
    --edge: #bdbdbd;
  }
  * { box-sizing: border-box; margin: 0; padding: 0; }
  html, body {
    width: 1200px;
    height: 735px;
    overflow: hidden;
    background: var(--paper);
  }
  .card {
    position: relative;
    width: 1200px;
    height: 735px;
    background: var(--paper);
    border: 1px solid var(--edge);
    overflow: hidden;
    font-family: "Arimo", Arial, sans-serif;
    color: var(--ink);
  }
  .brand {
    position: absolute;
    left: 0;
    width: 676px;
    top: 274px;
    text-align: center;
  }
  .brand-mark {
    display: block;
    width: 144px;
    height: 144px;
    margin: 0 auto 4px;
  }
  .brand-name {
    font-size: 49px;
    font-weight: 400;
    color: var(--navy);
    letter-spacing: 0.2px;
    line-height: 1.15;
  }
  .divider {
    position: absolute;
    left: 650px;
    top: 124px;
    width: 7px;
    height: 487px;
    background: var(--rule);
  }
  .person {
    position: absolute;
    left: 715px;
    top: 116px;
  }
  .person-name {
    font-size: 36px;
    font-weight: 700;
    color: var(--navy);
    line-height: 1.1;
  }
  .person-title {
    font-size: 37px;
    font-weight: 400;
    color: var(--steel);
    line-height: 1.1;
  }
  .contact {
    position: absolute;
    left: 715px;
    display: flex;
    align-items: flex-start;
    gap: 14px;
    font-size: 31px;
    line-height: 41px;
    color: var(--ink);
  }
  .contact-icon {
    flex: none;
    width: 24px;
    height: 34px;
    margin-top: 4px;
  }
  .contact--address { top: 338px; }
  .contact--phone { top: 502px; }
  .base-band {
    position: absolute;
    left: 0;
    bottom: 0;
    width: 1200px;
    height: 62px;
  }
</style>
</head>
<body>
  <main class="card">
    <section class="brand">
      <svg class="brand-mark" viewBox="0 0 144 144" aria-hidden="true">
        <circle cx="72" cy="72" r="70" fill="var(--brand-blue)"/>
      </svg>
      <h1 class="brand-name">Morvane Equity LLC</h1>
    </section>

    <div class="divider"></div>

    <section class="person">
      <h2 class="person-name">Peter Dalby</h2>
      <p class="person-title">Portfolio Manager</p>
    </section>

    <p class="contact contact--address">
      <svg class="contact-icon" viewBox="0 0 24 34" aria-hidden="true">
        <path d="M12 3a8 8 0 0 0-8 8c0 6 8 16 8 16s8-10 8-16a8 8 0 0 0-8-8z" fill="none" stroke="var(--ink)" stroke-width="2.6"/>
        <circle cx="12" cy="11" r="2.8" fill="var(--ink)"/>
      </svg>
      <span>2650 Birchmont Lane,<br>Suite 300, Atlanta GA<br>30327</span>
    </p>

    <p class="contact contact--phone">
      <svg class="contact-icon" viewBox="0 0 24 34" aria-hidden="true">
        <rect x="4" y="3" width="16" height="28" rx="3" fill="none" stroke="var(--ink)" stroke-width="2.4"/>
        <circle cx="12" cy="26" r="1.6" fill="var(--ink)"/>
      </svg>
      <span>(412) 555-0187</span>
    </p>

    <svg class="base-band" viewBox="0 0 1200 62" preserveAspectRatio="none" aria-hidden="true">
      <path d="M0 62 Q600 -56 1200 62 Z" fill="var(--navy)"/>
    </svg>
  </main>
</body>
</html>
```